Byteloft - Your IT support team - online sales website design concept

Byteloft aims to provide home and small business users with high quality, friendly and affordable IT support.

We are delivering this service through the website. Users will choose a support service that they want, enter some details, make a payment and then be connected to our support team member who will resolve their problem and discuss their IT with them by remotely controlling their computer and speaking to them on the phone.

This design project is to develop the website design concept which will:

# Give the user confidence that byteloft are a legitimate business giving premium yet good value IT support.
# Inform the users of our IT services.
# Encourage the user to try our services.
# Look fun, interesting, modern, respectable and trustworthy.

We intend to offer 4 core 'products' to our users, these are:
# Virus removal – We will clean your PC then protect it for the future
# Computer Speed Up – Optimise you PC to get the most out of it
# Skyvault your IT- auto backup of PC with remote access to documents, pictures, videos and email
# IT Support – to fix a problem or we can just help out

We are open to any fun or interesting ways of getting this message across to users.

We have the following idea which could be useful but does not have to be used in design concepts:

Perhaps a home/detached house on the front page with a cloud in the sky for our cloud service, a fast car on the drive or something to demonstrate computer speed up, a gremlin in the drain for virus removal and our byteloft yellow waves from our logo emanating towards the house as our general IT support offering. Maybe having some movement or information on mouse over.

We like the idea of real life images embedded into the page similar to this:

http://www.prolivasad.cz/

But, ideas could be cartoon based or whatever you think will look good. Any interesting concepts are welcome.

We want to have our 4 'products' clearly displayed on the home page. They could be in 4 boxes beneath some nice image or incorporated into a single nice image/cartoon or graphic. If incorporated into one graphic/cartoon/image we would have clickable areas of the image.

We want it to be clear to visitors what it is we are offering - IT support to remotely solve a computer/iPad/smartphone issue and that we are "Online now to fix your problem".

We might also want to feature 4 features/benefits:

UK Based Engineers (with GB flag)
Remote IT Support
Premium Support
Money Back Guarantee

We have a logo already which is attached. We would like a homepage design encompassing the features set out above, a second page design to be used as the main page when you click on one of the 4 'products' and also a general content page design so that we have a theme for the site. We just want these designs as images for this project.

Thank you for your interest.

Reason: 10 days was never long enough and we needed more time to respond to designers.

Reason: I've been away on holiday and I want some more time to respond to designers. Thanks, Colin

Target Market(s)

Home and small business users.

Industry/Entity Type

Small Business

Requirements
Must have
• We would like an area, to show whether we are open and online or not. When staff are available to deliver remote support the site should clearly show that staff are online working and available now to support. When we are offline the site should also show this.

We will offer our users a "Money Back Guarantee"; if they are not happy with the work that we do for them we will refund them.

```html
<!DOCTYPE html>
<html lang="en">
<head>
<meta charset="utf-8">
<title>Byteloft – Get IT Support Now</title>
<link rel="stylesheet" href="https://fonts.googleapis.com/css2?family=Ubuntu:wght@400;500;700&family=Oswald:wght@500&family=Arimo:wght@400&display=swap">
<style>
  :root {
    --brand-yellow: #fbbf2d;
    --panel-yellow: #fecb00;
    --ink: #1a1a1a;
    --ink-soft: #3a3a3a;
    --nav-bg: #111111;
    --nav-bg-top: #2a2a2a;
    --white: #ffffff;
    --muted: #bdbdbd;
    --radio-blue: #2f6fb7;
  }
  * { box-sizing: border-box; margin: 0; padding: 0; }
  html, body { width: 1200px; height: 970px; overflow: hidden; background: var(--white); }
  body { position: relative; font-family: "Ubuntu", sans-serif; color: var(--ink); }

  .topbar {
    position: absolute; left: 0; top: 0; width: 1200px; height: 36px;
    background: linear-gradient(var(--nav-bg-top), var(--nav-bg));
    font-family: "Oswald", sans-serif; font-size: 14px; color: var(--white);
  }
  .topbar a { position: absolute; top: 0; line-height: 36px; color: inherit; text-decoration: none; letter-spacing: 0.2px; }
  .topbar .is-active { background: var(--panel-yellow); color: var(--ink); width: 76px; text-align: center; }
  .topbar .is-active::before {
    content: ""; position: absolute; left: 32px; top: 0;
    border-left: 6px solid transparent; border-right: 6px solid transparent; border-top: 6px solid var(--nav-bg);
  }
  .topbar .sign-in { color: var(--brand-yellow); }
  .topbar .support { color: var(--muted); }
  .topbar .divider { position: absolute; left: 938px; top: 11px; width: 1px; height: 14px; background: var(--muted); }
  .social { position: absolute; display: flex; gap: 10px; }
  .social span { width: 14px; height: 14px; border-radius: 50%; background: var(--muted); }

  .masthead {
    position: absolute; left: 0; top: 36px; width: 1200px; height: 168px;
    box-shadow: 0 12px 14px -10px rgba(0,0,0,0.18);
  }
  .brand { position: absolute; left: 182px; top: 60px; display: flex; align-items: center; gap: 14px; }
  .brand-mark { width: 30px; height: 30px; background: var(--brand-yellow); }
  .brand-name { font-weight: 500; font-size: 54px; line-height: 1; color: var(--ink); }
  .slogan { position: absolute; right: 207px; top: 48px; text-align: right; }
  .slogan-small { font-size: 25px; font-weight: 500; color: var(--ink-soft); line-height: 1.2; }
  .slogan-large { font-size: 41px; font-weight: 500; line-height: 1.1; color: var(--ink); }

  .page-title { position: absolute; left: 184px; top: 268px; font-size: 38px; font-weight: 500; }
  .page-lead { position: absolute; left: 185px; top: 317px; font-size: 19px; color: var(--ink-soft); }

  .form-panel { position: absolute; left: 183px; width: 803px; background: var(--panel-yellow); font-size: 19px; }
  .question { height: 99px; }
  .question-text { position: absolute; left: 39px; top: 50%; transform: translateY(-50%); }
  .choice { position: absolute; top: 50%; transform: translateY(-50%); display: flex; align-items: center; gap: 8px; }
  .radio { width: 11px; height: 11px; border-radius: 50%; border: 1px solid #9bb3c9; background: var(--white); }
  .radio.is-checked { background: radial-gradient(circle, var(--radio-blue) 0 2.5px, var(--white) 3px); }

  .details { top: 596px; height: 126px; }
  .field-label { position: absolute; left: 39px; }
  .field-input { position: absolute; left: 191px; width: 320px; height: 36px; background: var(--white); }
  .submit {
    position: absolute; left: 641px; top: 67px; width: 143px; height: 36px; background: var(--nav-bg);
    color: var(--white); font-family: "Oswald", sans-serif; font-size: 20px; display: flex; align-items: center; gap: 16px; padding-left: 18px;
  }

  .footer {
    position: absolute; left: 0; top: 876px; width: 1200px; height: 94px;
    background: linear-gradient(var(--nav-bg-top), var(--nav-bg) 40%); color: var(--white);
  }
  .footer-links { position: absolute; top: 19px; list-style: none; font-family: "Arimo", sans-serif; font-size: 11px; line-height: 19px; }
  .footer-copy { position: absolute; left: 566px; top: 57px; font-family: "Arimo", sans-serif; font-size: 11px; }
  .footer-brand { position: absolute; left: 832px; top: 30px; display: flex; gap: 10px; align-items: center; }
  .footer-brand .brand-mark { width: 18px; height: 18px; }
  .footer-brand .brand-name { font-size: 32px; color: var(--white); }
</style>
</head>
<body>
  <nav class="topbar">
    <a style="left:198px">HOME</a>
    <a style="left:258px">ABOUT US</a>
    <a class="is-active" style="left:321px">IT SUPPORT</a>
    <a style="left:409px">WEB REMOTE SUPPORT</a>
    <a style="left:544px">BLOG</a>
    <a style="left:588px">CONTACT</a>
    <div class="social" style="left:776px; top:11px"><span></span><span></span><span></span></div>
    <a class="sign-in" style="left:891px">SIGN IN</a>
    <span class="divider"></span>
    <a class="support" style="left:949px">SUPPORT</a>
  </nav>

  <header class="masthead">
    <div class="brand"><span class="brand-mark"></span><span class="brand-name">Byteloft</span></div>
    <div class="slogan">
      <p class="slogan-small">high quality, friendly and</p>
      <p class="slogan-large">affordable IT support</p>
    </div>
  </header>

  <main>
    <h1 class="page-title">Get IT Support Now!</h1>
    <p class="page-lead">Please fill up the form to Proceed</p>

    <section class="form-panel question" style="top:375px">
      <p class="question-text">Are you on the computer that needs support?</p>
      <span class="choice" style="left:639px"><span class="radio is-checked"></span>Yes</span>
      <span class="choice" style="left:716px"><span class="radio"></span>No</span>
    </section>

    <section class="form-panel question" style="top:485px">
      <p class="question-text">Is the computer that needs fixing connected to the internet?</p>
      <span class="choice" style="left:639px"><span class="radio is-checked"></span>Yes</span>
      <span class="choice" style="left:716px"><span class="radio"></span>No</span>
    </section>

    <section class="form-panel details">
      <span class="field-label" style="top:26px">Your Full Name</span>
      <span class="field-input" style="top:18px"></span>
      <span class="field-label" style="top:74px">Email address</span>
      <span class="field-input" style="top:67px"></span>
      <span class="submit">
        <svg width="14" height="12" viewBox="0 0 14 12" aria-hidden="true"><path d="M1 1l5 5-5 5M7 1l5 5-5 5" fill="none" stroke="#fff" stroke-width="2"/></svg>
        SUBMIT
      </span>
    </section>
  </main>

  <footer class="footer">
    <ul class="footer-links" style="left:206px"><li>About</li><li>IT Support</li><li>Blogs</li></ul>
    <ul class="footer-links" style="left:284px"><li>Legal</li><li>Jobs</li><li>Sitemap</li></ul>
    <div class="social" style="left:590px; top:29px"><span></span><span></span><span></span></div>
    <p class="footer-copy">© 2013 Byteloft.com</p>
    <div class="footer-brand"><span class="brand-mark"></span><span class="brand-name">Byteloft</span></div>
  </footer>
</body>
</html>
```